Folded Business Cards for Guarantee, Layaway & The Fine Print

I am looking for a set of (3) folded business for our guarantee, layaway and fine print policies. I would like the same design for each of these cards, with the exception of the picture, title and verbiage.
The front of each card must include our logo, the title of the card (Our Guarantee, Layaway or The Fine Print,) and a picture of a piece of jewelry. The inside of the card should state our policies. The back of the card should have our logo, address (Bellstone Court #9, Alderbrook, VT 05999,) phone # (555-281-0947) email & web address (info@vantorgems.com, www.vantorgems.com) and social media icons (FB, Twitter, Pinterest, Instagram)

The layaway card needs a place for the customer's signature.

I was thinking the orientation of the card should be vertical but if the right design ends up being horizontal, I'm ok with that. I do have concerns about readability and that this may be too much information for a folded business card. So, I am open to either changing the front & back, if need be or going to a different format (standard postcard size. Verbiage may also need to be trimmed down, but I need to know what is possible first.

Our branding colors are espresso brown & coppery orange so please do not stray from this color palette. The font of our logo is joefin. I would like the verbiage of the cards to be in quattrocento sans font. We would like a modern & clean look please.

Attached, please find our logo, policies and jewelry pictures. For picture placement, please do the following: Layaway Card (Quartz & onyx pendant,) The Fine Print Card (Orange Garnet Pendant,) Our Guarantee (triple Green Tourmaline Ring.)

```html
<!DOCTYPE html>
<html lang="en">
<head>
<meta charset="utf-8">
<title>Vantor Gems – Our Guarantee folded card</title>
<link rel="stylesheet" href="https://fonts.googleapis.com/css2?family=Quattrocento+Sans:wght@400;700&display=swap">
<style>
  :root {
    --espresso: #45271d;
    --espresso-deep: #3a2018;
    --paper: #f2efee;
    --ink: #5a2e22;
    --cream: #ffffff;
    --stage: #ffffff;
    --gold: #c9a13a;
    --tourmaline: #3f6a2a;
  }
  * { box-sizing: border-box; margin: 0; padding: 0; }
  html, body { width: 1200px; height: 1000px; overflow: hidden; background: var(--stage); }
  body { position: relative; font-family: "Quattrocento Sans", Arial, sans-serif; }

  .spread {
    position: absolute; top: 120px; width: 560px; height: 760px;
    display: flex; box-shadow: 0 4px 18px rgba(0,0,0,.18);
  }
  .spread--outside { left: 25px; }
  .spread--inside { left: 615px; }
  .panel { position: relative; width: 280px; height: 100%; }

  /* Outside */
  .panel--back, .panel--front { background: var(--espresso); color: var(--cream); }
  .panel--back { border-right: 1px solid var(--espresso-deep); padding: 80px 24px 0 36px; }
  .brand-name {
    font-family: "Quattrocento Sans", Arial, sans-serif; font-weight: 400;
    font-size: 38px; line-height: 1.1; white-space: nowrap; margin-bottom: 56px;
  }
  .contact { list-style: none; font-size: 20px; line-height: 1.3; }
  .contact li { display: flex; gap: 10px; margin-bottom: 22px; }
  .contact svg { flex: none; width: 20px; height: 20px; margin-top: 2px; fill: var(--cream); }
  .contact .stroke { fill: none; stroke: var(--cream); stroke-width: 1.6; }
  .social { position: absolute; left: 0; right: 0; bottom: 110px; display: flex; justify-content: center; gap: 8px; }
  .social span { width: 24px; height: 24px; border-radius: 4px; background: var(--cream); }
  .web { position: absolute; left: 0; right: 0; bottom: 70px; text-align: center; font-size: 19px; }

  .card-title {
    text-align: center; font-weight: 700; font-size: 32px; margin-top: 140px;
  }
  .jewel-photo {
    width: 160px; height: 290px; margin: 60px auto 0; border-radius: 10px;
    background: linear-gradient(180deg, #d9c9a0 0%, var(--tourmaline) 30%, var(--gold) 55%, var(--tourmaline) 75%, #6b6a66 100%);
  }

  /* Inside */
  .panel--left, .panel--right { background: var(--paper); color: var(--ink); }
  .panel--left { border-right: 1px solid #d8d2d0; }
  .promise-band {
    height: 74px; background: var(--espresso); color: var(--cream);
    font-size: 25px; padding: 22px 0 0 22px;
  }
  .panel--right .promise-band { padding: 0; }
  .policy { padding: 26px 22px 0 24px; font-size: 18.5px; line-height: 1.3; }
  .policy p { margin-bottom: 26px; }
</style>
</head>
<body>

<section class="spread spread--outside">
  <div class="panel panel--back">
    <h1 class="brand-name">Vantor Gems</h1>
    <ul class="contact">
      <li>
        <svg viewBox="0 0 20 20" aria-hidden="true"><path d="M10 2 1 10h3v8h5v-5h2v5h5v-8h3z"/></svg>
        <span>Bellstone Court #9,<br>Alderbrook,<br>VT 05999.</span>
      </li>
      <li>
        <svg viewBox="0 0 20 20" aria-hidden="true"><path d="M5 1c1 0 3 4 3 5s-2 1.5-2 2.5 3 5 4 5.5 1.5-1.5 2.5-1.5 4.5 2 4.5 3-2 3-3.5 3C7 18 2 11 2 5c0-2 2-4 3-4z"/></svg>
        <span>555-281-0947</span>
      </li>
      <li>
        <svg viewBox="0 0 20 20" aria-hidden="true"><rect class="stroke" x="1.5" y="4" width="17" height="12"/><path class="stroke" d="M1.5 4 10 11l8.5-7M1.5 16l6-6M18.5 16l-6-6"/></svg>
        <span>info@vantorgems.com</span>
      </li>
    </ul>
    <div class="social" aria-label="Social media"><span></span><span></span><span></span><span></span></div>
    <p class="web">www.vantorgems.com</p>
  </div>
  <div class="panel panel--front">
    <h2 class="card-title">Our Guarantee</h2>
    <div class="jewel-photo" role="img" aria-label="Photo of a triple green tourmaline ring with gold bezels and diamonds"></div>
  </div>
</section>

<section class="spread spread--inside">
  <div class="panel panel--left">
    <div class="promise-band">Our Promise to You...</div>
    <div class="policy">
      <p>Vantor's guarantees your jewelry purchase for 2 years from date of purchase.</p>
      <p>We will repair or replace any piece of jewelry that is determined to be defective in materials and/or workmanship.</p>
      <p>We will repair or replace any stone loss up to 0.20ct. per stone, due to defects in materials and/or workmanship.</p>
      <p>Our jewelry repairs are guaranteed for 6 months from completion date.</p>
    </div>
  </div>
  <div class="panel panel--right">
    <div class="promise-band"></div>
    <div class="policy">
      <p>Our watch repairs are guaranteed for 90 days from completion date. We do not warranty watches against water damage.</p>
      <p>we offer free lifetime cleaning &amp; inspection of your jewelry from Vantor's. We'll make sure everything is safe &amp; secure and, of course, sparkling. You should do this at least every six months.</p>
      <p>Above all, we want you to be pleased with your jewelry purchase or repair from Vantor's. If you have any questions or concerns, please never hesitate to speak to us.</p>
    </div>
  </div>
</section>

</body>
</html>
```